Design für Eisverpackung
Zielgruppe
Wir sind ein kleiner regionaler Eisproduzent, betreiben ein Eiscafe mit eigener Produktion. Wir füllen unsere Produkte in Plaste- bzw. Hartpapierbechern ab und vermarkten sie im Einzelhandel, Tankstellen und zu Festen aller Art. Wir benötigen für eine neue Eisverpackung ein ansprechendes und modernes Design.
Aufgabenstellung
Bei der neuen Verpackungseinheit handelt es sich um einen 130ml Hartpapierbecher (Foto Anhang).
Die Designgestaltung umfasst den Becher und ein Rundetikett, welches auf den Becherdeckel platziert wird. Der Becherdeckel selber bleibt neutral weiß,er soll nur mit dem Rundetikett (Durchmesser ca. 6cm) beklebt werden. Eine Skizze als Designvorlage (Becher) finden Sie im Anhang unten. Das Design soll ein hochwertiges Produkt wieder spiegeln.
Bei der Gestaltung des Bechers haben wir schon konkrete Vorstellungen. Der Becher sollte Eissorten-neutral gestaltet werden, da er bei der Verpackung verschiedener Geschmacksrichtungen Anwendung findet.
Des weiteren die Einarbeitung unseres Logo´s (Anhang), der Name des Produktes ("Süßer Moment")und die Bezeichnung Milcheis. Farblich soll der Becher die Farben Hellblau als Grundfarbe und Gelb haben. Der Name " Süßer Moment" vielleicht in rot.
Es müssen auf der Becherrückseite Freiflächen berücksichtigt werden, auf denen wir Informationen wie Inhaltsstoffe und Nährwerte etc. platzieren können.
Die Deckelgestaltung soll im Design natürlich harmonisch zum Gesamtbecher passen.
Zu berücksichtigen ist lediglich, das auf dem Deckel eine Freifläche vorhanden seien muss,
auf der die entsprechende Eissorte Platz findet. Diese wird von uns per Thermodruck entsprechend auf das Deckeletikett platziert.

```html
<!DOCTYPE html>
<html lang="de">
<head>
<meta charset="utf-8">
<title>Süßer Moment – Milcheis Becher und Deckeletikett</title>
<link rel="stylesheet" href="https://fonts.googleapis.com/css2?family=Pacifico&family=Dancing+Script:wght@600;700&family=Nunito:wght@800&family=Roboto+Slab:ital@0;1&display=swap">
<style>
  :root {
    --sky-deep: #4fb3d9;
    --sky-light: #d7eef7;
    --cream: #fbf6dc;
    --sun: #f3d36a;
    --milk: #ffffff;
    --title-red: #c4261c;
    --title-shadow: #7d1610;
    --milcheis-blue: #1e5aa8;
    --ribbon-dark: #b8792a;
    --ribbon-light: #f2c64f;
    --brand-green: #a9c75a;
    --ink: #333333;
    --page: #ffffff;
  }
  html, body {
    margin: 0;
    width: 1200px;
    height: 841px;
    overflow: hidden;
    background: var(--page);
  }
  .sheet {
    position: relative;
    width: 1200px;
    height: 841px;
  }
  .lid-label {
    position: absolute;
    left: 50px;
    top: 150px;
    width: 540px;
    height: 540px;
  }
  .cup-wrap {
    position: absolute;
    left: 590px;
    top: 230px;
    width: 590px;
    height: 380px;
  }
  .brand-name {
    font-family: "Nunito", sans-serif;
    font-weight: 800;
    fill: var(--brand-green);
  }
  .product-title {
    font-family: "Pacifico", cursive;
    fill: var(--title-red);
    stroke: var(--milk);
    stroke-width: 3;
    paint-order: stroke;
  }
  .product-type {
    font-family: "Dancing Script", cursive;
    font-weight: 700;
    fill: var(--milk);
    stroke: var(--milcheis-blue);
    stroke-width: 1.6;
  }
  .ribbon-text {
    font-family: "Dancing Script", cursive;
    font-weight: 700;
    fill: var(--milk);
  }
  .info-text {
    font-family: "Roboto Slab", serif;
    fill: var(--ink);
  }
  .weight-text {
    font-family: "Roboto Slab", serif;
    font-style: italic;
    fill: var(--ink);
  }
</style>
</head>
<body>
<main class="sheet">

  <!-- Deckeletikett -->
  <svg class="lid-label" viewBox="0 0 540 540" aria-label="Rundetikett für den Deckel">
    <defs>
      <radialGradient id="lid-ring" cx="50%" cy="50%" r="50%">
        <stop offset="0.84" stop-color="#ffffff"/>
        <stop offset="1" stop-color="#8ccbe4"/>
      </radialGradient>
      <linearGradient id="lid-sky" x1="0" y1="0" x2="0" y2="1">
        <stop offset="0" stop-color="#4aaad3"/>
        <stop offset="0.3" stop-color="#e9f6fb"/>
        <stop offset="0.55" stop-color="#fbf3cf"/>
        <stop offset="0.8" stop-color="#f1c95a"/>
      </linearGradient>
      <radialGradient id="lid-splash" cx="50%" cy="35%" r="60%">
        <stop offset="0.4" stop-color="#ffffff"/>
        <stop offset="1" stop-color="#eef2f4"/>
      </radialGradient>
      <linearGradient id="ribbon" x1="0" y1="0" x2="1" y2="0">
        <stop offset="0" stop-color="var(--ribbon-dark)"/>
        <stop offset="0.5" stop-color="#e0a345"/>
        <stop offset="1" stop-color="var(--ribbon-light)"/>
      </linearGradient>
      <clipPath id="lid-inner"><circle cx="270" cy="270" r="235"/></clipPath>
    </defs>

    <circle cx="270" cy="270" r="268" fill="url(#lid-ring)"/>
    <g clip-path="url(#lid-inner)">
      <rect x="30" y="30" width="480" height="480" fill="url(#lid-sky)"/>
      <path role="img" aria-label="Milchspritzer" d="M30 330 C110 300 150 360 210 340 C290 310 330 360 400 330 C450 310 490 330 510 320 L510 510 L30 510 Z" fill="url(#lid-splash)"/>
    </g>
    <circle cx="270" cy="270" r="235" fill="none" stroke="#ffffff" stroke-width="3"/>

    <g class="brand">
      <circle cx="212" cy="120" r="12" fill="var(--brand-green)"/>
      <text class="brand-name" x="232" y="131" font-size="30">Talbrunn</text>
    </g>

    <text class="product-title" x="270" y="228" font-size="58" text-anchor="middle" transform="rotate(-4 270 228)">Süßer</text>
    <text class="product-title" x="275" y="318" font-size="82" text-anchor="middle" transform="rotate(-4 275 318)">Moment</text>
    <text class="product-type" x="320" y="372" font-size="50" text-anchor="middle" transform="rotate(-6 320 372)">Milcheis</text>

    <path d="M55 402 L325 388 L312 432 L42 446 Z" fill="url(#ribbon)"/>
    <text class="ribbon-text" x="185" y="432" font-size="40" text-anchor="middle" transform="rotate(-3 185 432)">Vanilla</text>
  </svg>

  <!-- Becherabwicklung -->
  <svg class="cup-wrap" viewBox="0 0 640 380" aria-label="Abwicklung des Becherdrucks">
    <defs>
      <linearGradient id="wrap-sky" x1="0" y1="0" x2="0" y2="1">
        <stop offset="0" stop-color="#4aaad3"/>
        <stop offset="0.35" stop-color="#e9f6fb"/>
        <stop offset="0.65" stop-color="#fbf3cf"/>
        <stop offset="1" stop-color="#f1c95a"/>
      </linearGradient>
      <radialGradient id="wrap-splash" cx="50%" cy="30%" r="70%">
        <stop offset="0.4" stop-color="#ffffff"/>
        <stop offset="1" stop-color="#eef2f4"/>
      </radialGradient>
      <linearGradient id="wrap-ribbon" x1="0" y1="0" x2="1" y2="0">
        <stop offset="0" stop-color="var(--ribbon-dark)"/>
        <stop offset="0.5" stop-color="#e0a345"/>
        <stop offset="1" stop-color="var(--ribbon-light)"/>
      </linearGradient>
      <clipPath id="wrap-shape">
        <path d="M8 32.8 A1500 1500 0 0 1 632 32.8 L570.5 326.2 A1200 1200 0 0 0 70.5 326.2 Z"/>
      </clipPath>
    </defs>

    <g clip-path="url(#wrap-shape)">
      <rect x="0" y="0" width="640" height="380" fill="url(#wrap-sky)"/>
      <path role="img" aria-label="Milchspritzer" d="M0 230 C60 200 110 250 170 225 C220 205 260 240 300 220 L300 380 L0 380 Z" fill="url(#wrap-splash)"/>
      <path role="img" aria-label="Milchspritzer" d="M345 225 C400 200 450 245 510 220 C560 200 600 230 640 215 L640 380 L345 380 Z" fill="url(#wrap-splash)"/>

      <!-- Vorderseite links -->
      <circle cx="120" cy="70" r="7" fill="var(--brand-green)"/>
      <text class="brand-name" x="132" y="77" font-size="18">Talbrunn</text>
      <text class="product-title" x="160" y="140" font-size="34" text-anchor="middle" transform="rotate(-6 160 140)">Süßer</text>
      <text class="product-title" x="165" y="192" font-size="46" text-anchor="middle" transform="rotate(-6 165 192)">Moment</text>
      <text class="product-type" x="205" y="228" font-size="30" text-anchor="middle" transform="rotate(-8 205 228)">Milcheis</text>
      <path d="M60 300 L200 268 L196 292 L56 324 Z" fill="url(#wrap-ribbon)"/>
      <text class="ribbon-text" x="128" y="304" font-size="20" text-anchor="middle" transform="rotate(-12 128 304)">hmm… lecker</text>

      <!-- Freifläche Rückseite -->
      <rect x="312" y="68" width="46" height="220" fill="#ffffff"/>
      <text class="info-text" font-size="5.5">
        <tspan x="316" y="80" font-weight="700">Zutaten:</tspan>
        <tspan x="316" y="89">Milch, Sahne, Zucker,</tspan>
        <tspan x="316" y="97">Glukose, Magermilch,</tspan>
        <tspan x="316" y="105">Eigelb, Vanille,</tspan>
        <tspan x="316" y="113">Stabilisator, Emulgator,</tspan>
        <tspan x="316" y="121">Aroma, Farbstoff.</tspan>
      </text>
      <rect x="322" y="250" width="18" height="18" fill="var(--sun)"/>
      <text class="weight-text" x="335" y="284" font-size="11" text-anchor="middle">130g</text>

      <!-- Vorderseite rechts -->
      <circle cx="475" cy="68" r="7" fill="var(--brand-green)"/>
      <text class="brand-name" x="487" y="75" font-size="18">Talbrunn</text>
      <text class="product-title" x="505" y="135" font-size="34" text-anchor="middle" transform="rotate(4 505 135)">Süßer</text>
      <text class="product-title" x="500" y="186" font-size="46" text-anchor="middle" transform="rotate(4 500 186)">Moment</text>
      <text class="product-type" x="525" y="222" font-size="30" text-anchor="middle" transform="rotate(2 525 222)">Milcheis</text>
      <path d="M395 252 L545 246 L542 270 L392 276 Z" fill="url(#wrap-ribbon)"/>
      <text class="ribbon-text" x="465" y="268" font-size="20" text-anchor="middle" transform="rotate(-2 465 268)">hmm… lecker</text>
    </g>
  </svg>

</main>
</body>
</html>
```